Flyer Design for Private Car Service

Flyer should cater to Business Travelers and Executives who travel Business Class or First Class.
Flyer should include images attached.
Flyer should include the below text
Dallas to Austin
Chauffeured SUVs
• Travel Dallas to Austin in a new 2025 Marlow Strider for $499 one-way
• Trip includes a Uniformed Chauffeur who has a Commercial Drivers License (CDL)
• You can Schedule Chauffeur Pickup at Your Home in Dallas
• Our Chauffeur will Drop You Off at Your Final Destination in Austin
• You can Schedule Chauffeur Return Pickup in Austin and Return Back to Dallas.
• We offer Faster Times on Door-to-Door Travel than Bluecrest Airways
• We offer Comparable Prices on Door-to-Door Travel Times than Bluecrest Airways
• All of our trips are insured with $500k of commercial auto insurance
• Our Passengers can Talk on Cell Phone & Conduct Quill calls Throughout Travel
• Our Passengers have Maximum Privacy, Comfort and First-Class Amenities.
• Our Passengers Avoid Harwick Vale Field and KPR Airport hassles & delays
• Member Brenton Chamber of Commerce, Larkmoor Chamber of Commerce.
• Book your trip today at www.ridemarquel.example
Target Market(s)
Business Travelers
Look and feel
Each slider illustrates characteristics of the customer's brand and the style your logo design should communicate.

```html
<!DOCTYPE html>
<html lang="en">
<head>
<meta charset="utf-8">
<title>Marquel Rides – Dallas to Austin Flyer</title>
<link href="https://fonts.googleapis.com/css2?family=Open+Sans:wght@400;600;700;800&display=swap" rel="stylesheet">
<style>
  :root {
    --red: #e3202b;
    --red-deep: #c8151f;
    --ink: #1d1d1f;
    --text: #3a3a3c;
    --paper: #f4f1ee;
    --stage: #e6e1dc;
    --tick: #3fbf6a;
    --gold: #f2c230;
  }
  * { box-sizing: border-box; margin: 0; padding: 0; }
  html, body { width: 1200px; height: 900px; overflow: hidden; }
  body {
    background: var(--stage);
    font-family: "Open Sans", Arial, sans-serif;
    display: flex; align-items: center; justify-content: center;
  }
  .flyer {
    position: relative;
    width: 610px; height: 860px;
    background: var(--paper);
    overflow: hidden;
    color: var(--ink);
  }
  .hero-backdrop {
    position: absolute; inset: 0 0 auto 0; height: 420px;
    background: linear-gradient(180deg, #d9d6d4 0%, #ebe8e5 55%, var(--paper) 100%);
    opacity: .85;
  }
  .accent-pill {
    position: absolute; height: 14px; background: var(--red); border-radius: 7px;
  }
  .accent-pill--top { left: -10px; top: 22px; width: 140px; }
  .accent-pill--side { right: -10px; top: 372px; width: 100px; }

  .brand {
    position: absolute; top: 42px; right: 40px;
    display: flex; align-items: center; gap: 12px;
  }
  .brand__name {
    font-weight: 700; font-size: 30px; letter-spacing: 3px;
    text-transform: uppercase; color: var(--ink);
  }
  .brand__mark { width: 34px; height: 34px; border-radius: 50%; background: var(--red); }

  .headline {
    position: absolute; left: 40px; top: 118px; width: 320px;
  }
  .headline__tagline {
    color: var(--red); font-weight: 800; font-size: 27px; line-height: 1.15;
  }
  .headline__rule { height: 3px; background: var(--red); width: 290px; margin: 12px 0 14px; }
  .headline__route {
    font-weight: 800; font-size: 27px; line-height: 1.15; color: var(--ink);
  }
  .headline__price { color: var(--red); }

  .photo-cluster { position: absolute; left: 340px; top: 110px; }

  .section-band {
    position: absolute; left: 0; height: 44px; width: 560px;
    background: var(--red);
    clip-path: polygon(0 0, 100% 0, calc(100% - 22px) 100%, 0 100%);
    color: #fff; font-weight: 800; font-size: 23px;
    display: flex; align-items: center; padding-left: 40px;
  }
  .section-band--why { top: 412px; }
  .section-band--comfort { top: 570px; width: 470px; }
  .section-band--safety { top: 690px; width: 400px; }

  .benefits {
    position: absolute; left: 40px; list-style: none;
    font-size: 13.5px; line-height: 1.65; color: var(--text);
  }
  .benefits--why { top: 470px; }
  .benefits--comfort { top: 626px; }
  .benefits--safety { top: 746px; }
  .benefits li { display: flex; align-items: center; gap: 8px; }
  .benefits strong { color: var(--ink); font-weight: 700; }
  .benefits svg { flex: none; }

  .footer {
    position: absolute; left: 0; right: 0; bottom: 0; height: 76px;
    background: linear-gradient(90deg, var(--red-deep), var(--red));
    color: #fff; display: flex; justify-content: space-between; align-items: center;
    padding: 0 40px;
  }
  .footer__members { font-size: 12.5px; line-height: 1.5; }
  .footer__members strong { font-weight: 700; }
  .footer__cta { text-align: right; }
  .footer__cta-label { font-weight: 800; font-size: 19px; }
  .footer__url { font-size: 13px; }
</style>
</head>
<body>
  <main class="flyer">
    <div class="hero-backdrop" role="img" aria-label="Soft-focus photo of a luxury SUV interior"></div>
    <div class="accent-pill accent-pill--top"></div>
    <div class="accent-pill accent-pill--side"></div>

    <header class="brand">
      <span class="brand__name">Marquel Rides</span>
      <span class="brand__mark"></span>
    </header>

    <section class="headline">
      <h1 class="headline__tagline">Your First-Class Road Travel Solution</h1>
      <div class="headline__rule"></div>
      <p class="headline__route">Dallas to Austin<br>Chauffeured SUVs<br><span class="headline__price">$499</span> One-Way</p>
    </section>

    <svg class="photo-cluster" width="260" height="300" viewBox="0 0 260 300">
      <defs>
        <linearGradient id="photoA" x1="0" y1="0" x2="1" y2="1">
          <stop offset="0" stop-color="#9a9ea6"/><stop offset="1" stop-color="#2e3035"/>
        </linearGradient>
        <linearGradient id="photoB" x1="0" y1="0" x2="1" y2="1">
          <stop offset="0" stop-color="#c9ccd1"/><stop offset="1" stop-color="#3a3c42"/>
        </linearGradient>
        <linearGradient id="photoC" x1="0" y1="0" x2="0" y2="1">
          <stop offset="0" stop-color="#e4e5e8"/><stop offset="1" stop-color="#7d8088"/>
        </linearGradient>
      </defs>
      <g role="img" aria-label="Uniformed chauffeurs standing beside an SUV">
        <circle cx="170" cy="78" r="70" fill="url(#photoA)" stroke="var(--red)" stroke-width="5"/>
      </g>
      <g role="img" aria-label="Chauffeur opening the SUV door for a business traveler">
        <circle cx="78" cy="140" r="70" fill="url(#photoB)" stroke="var(--red)" stroke-width="5"/>
      </g>
      <g role="img" aria-label="Black SUVs parked outside an office building">
        <circle cx="172" cy="222" r="70" fill="url(#photoC)" stroke="var(--red)" stroke-width="5"/>
      </g>
    </svg>

    <h2 class="section-band section-band--why">Why Fly When You Can Travel in Style?</h2>
    <ul class="benefits benefits--why">
      <li><svg width="14" height="14" viewBox="0 0 14 14"><circle cx="7" cy="7" r="7" fill="var(--tick)"/><path d="M3.8 7.2l2.2 2.1 4.2-4.4" fill="none" stroke="#fff" stroke-width="1.8"/></svg><span>Faster <strong>Door-to-Door Travel</strong> Compared to Bluecrest Airways.</span></li>
      <li><svg width="14" height="14" viewBox="0 0 14 14"><circle cx="7" cy="7" r="7" fill="var(--tick)"/><path d="M3.8 7.2l2.2 2.1 4.2-4.4" fill="none" stroke="#fff" stroke-width="1.8"/></svg><span><strong>Comparable Pricing</strong> with Airline Door-to-Door Travel Times.</span></li>
      <li><svg width="14" height="14" viewBox="0 0 14 14"><circle cx="7" cy="7" r="7" fill="var(--tick)"/><path d="M3.8 7.2l2.2 2.1 4.2-4.4" fill="none" stroke="#fff" stroke-width="1.8"/></svg><span>Avoid the Hassles and Delays of Harwick Vale Field &amp; KPR Airport.</span></li>
    </ul>

    <h2 class="section-band section-band--comfort">Unmatched Comfort &amp; Privacy</h2>
    <ul class="benefits benefits--comfort">
      <li><svg width="14" height="14" viewBox="0 0 14 14"><path d="M7 1l1.8 3.8 4.1.5-3 2.8.8 4.1L7 10.2 3.3 12.2l.8-4.1-3-2.8 4.1-.5z" fill="var(--gold)"/></svg><span>Conduct Quill Calls or Use Your Cell Phone Freely During Travel.</span></li>
      <li><svg width="14" height="14" viewBox="0 0 14 14"><path d="M7 1l1.8 3.8 4.1.5-3 2.8.8 4.1L7 10.2 3.3 12.2l.8-4.1-3-2.8 4.1-.5z" fill="var(--gold)"/></svg><span>Enjoy Maximum Privacy, Comfort, and First-Class Amenities.</span></li>
    </ul>

    <h2 class="section-band section-band--safety">Safety You Can Trust</h2>
    <ul class="benefits benefits--safety">
      <li><svg width="14" height="14" viewBox="0 0 14 14"><path d="M7 1l5 2v4c0 3-2.2 5-5 6-2.8-1-5-3-5-6V3z" fill="var(--gold)"/></svg><span>$500k Commercial Auto Insurance Coverage for Every Trip.</span></li>
    </ul>

    <footer class="footer">
      <p class="footer__members">Proud Members Of - <strong>Brenton Chamber of Commerce</strong><br><strong>Larkmoor Chamber of Commerce</strong></p>
      <div class="footer__cta">
        <p class="footer__cta-label">Book Today</p>
        <p class="footer__url">www.ridemarquel.example</p>
      </div>
    </footer>
  </main>
</body>
</html>
```